Flash Website Intro
Animated flash intro for existing website with skip to site button
Hi Mira,
I sent you a private message regarding the updated link of my entry. Thanks
Tobin
Thank you for all your great work
I will now go through them with my partner and will let you know the decision
thanks
@Project Holder
Please check your private message and view my animation please.
http://vexloop.example/serve/5517302
Thanks
RunaFeld
dear sir,
i send link in private message. in that some clarity missing but real one is crystal clear
Hi PH, I sent you 2 link for #9
I sent you the link via private message.
for my entry#7
Hi,
Have you seen the animated version of my entry #5? I sent you the link via private message.
It is against the t&c's to send email address.
If you can upload to the internet and send me a link to view animation.
I won't be able to pick a design just from a static screenshot so please send me a link to view the full animation
thanks,
it's possible to see the animated result but we need to have ur personnal e-mail cauz here we cannot upload file larger than 2 mb . that's why
I have another doubt, banner or intro web, because I do not close their sizes
.gif format work here.
Hi
I have asked support how I view the animation rather than just a screenshot. Haven't had a response yet.
If anyone knows how I can view the flash files before I choose one please let me know
Hey i few questions:
How can uploads the swf´s
Or you want to take a screencapture of the intro.
Thank u
Please ignore the "Ad Sizes Required:" in the brief as it is just one flash banner size 880 x 325 (same as the white box on the home page of the website)

```html
<!DOCTYPE html>
<html lang="en">
<head>
<meta charset="utf-8">
<title>Clavora – Intro</title>
<link rel="stylesheet" href="https://fonts.googleapis.com/css2?family=Arimo:wght@400&display=swap">
<style>
  :root {
    --wall: #b2d198;
    --wall-top: #a9c98f;
    --floor: #cde9ad;
    --floor-edge: #c3e0a3;
    --panel-center: #ffffff;
    --panel-edge: #e1eed3;
    --brand-text: #3a3a3a;
    --tab: #e4e4e0;
    --tab-text: #333333;
  }
  html, body {
    margin: 0;
    padding: 0;
    width: 1200px;
    height: 607px;
    overflow: hidden;
  }
  .stage {
    position: relative;
    width: 1200px;
    height: 607px;
    background: linear-gradient(to bottom, var(--wall-top) 0, var(--wall) 276px, var(--floor-edge) 277px, var(--floor) 340px, var(--floor) 100%);
    overflow: hidden;
  }
  .floor-shadow {
    position: absolute;
    left: 200px;
    top: 380px;
    width: 800px;
    height: 44px;
    border-radius: 50%;
    background: radial-gradient(ellipse at center, rgba(20,30,10,0.8) 0%, rgba(20,30,10,0.4) 45%, rgba(20,30,10,0) 72%);
  }
  .intro-panel {
    position: absolute;
    left: 156px;
    top: 67px;
    width: 876px;
    height: 317px;
    background: radial-gradient(ellipse 60% 65% at 50% 48%, var(--panel-center) 0%, var(--panel-center) 45%, var(--panel-edge) 100%);
    overflow: hidden;
  }
  .brand-name {
    position: absolute;
    left: 0;
    right: 0;
    top: 102px;
    margin: 0;
    text-align: center;
    font-family: "Arimo", Arial, sans-serif;
    font-weight: 400;
    font-size: 72px;
    line-height: 1;
    color: var(--brand-text);
  }
  .skip-intro {
    position: absolute;
    left: 380px;
    bottom: 0;
    width: 116px;
    height: 32px;
    border-radius: 58px 58px 0 0;
    background: var(--tab);
    color: var(--tab-text);
    font-family: "Arimo", Arial, sans-serif;
    font-weight: 400;
    font-size: 13px;
    text-align: center;
    line-height: 30px;
    text-decoration: none;
  }
</style>
</head>
<body>
  <div class="stage">
    <div class="floor-shadow"></div>
    <section class="intro-panel">
      <h1 class="brand-name">Clavora</h1>
      <a class="skip-intro" href="#">skip intro</a>
    </section>
  </div>
</body>
</html>
```